Post Card Design Bright Lantern Youth

We need a postcard design that will be mailed to all residents offering free pickups of donated clothing. Our foundation is called Bright Lantern Youth, we are a nonprofit charitable organization that provides meals and medical services to children in need in Honduras. Collecting unwanted second-hand clothing generates revenue that helps fund the mission and programs run by our foundation. We would like to offer our pickup services to everyone who has any unwanted reusable clothing.

```html
<!DOCTYPE html>
<html lang="en">
<head>
<meta charset="utf-8">
<title>Bright Lantern Youth – Clothing Donation Postcard</title>
<link rel="stylesheet" href="https://fonts.googleapis.com/css2?family=Montserrat:ital,wght@1,900&family=Arimo:wght@400;700&display=swap">
<style>
  :root{
    --backdrop:#c1beb8;
    --paper:#ffffff;
    --pink:#e6088c;
    --blue:#0a8fd6;
    --green:#7dc242;
    --yellow:#ffc90a;
    --ink:#1a1a1a;
    --rule:#555555;
    --line-fill:#e6e6e6;
    --box-edge:#6f6f6f;
  }
  *{margin:0;padding:0;box-sizing:border-box}
  html,body{width:1200px;height:1200px;overflow:hidden;background:var(--backdrop)}
  .canvas{position:relative;width:1200px;height:1200px}
  .postcard{position:absolute;left:199px;width:722px;height:516px;background:var(--paper);overflow:hidden}
  .postcard--front{top:65px}
  .postcard--back{top:614px}

  .brand{position:absolute;left:26px;display:flex;flex-direction:column;align-items:center;gap:10px;width:180px}
  .brand__dot{width:44px;height:44px;border-radius:50%;background:var(--green)}
  .brand__name{font-family:Arimo,sans-serif;font-weight:700;font-size:19px;color:var(--green);white-space:nowrap}

  .headline{position:absolute;left:26px;font-family:Montserrat,sans-serif;font-style:italic;font-weight:900;font-size:35px;line-height:37px;letter-spacing:-1px}
  .headline span{display:block}
  .headline .pink{color:var(--pink)}
  .headline .blue{color:var(--blue)}

  .copy{position:absolute;left:28px;font-family:Arimo,sans-serif;font-size:14px;line-height:17px;color:var(--ink)}

  .services{position:absolute;left:32px;display:flex;gap:16px}
  .service-icon{width:55px;height:55px}

  .photo{position:absolute;left:0;top:0;width:722px;height:516px}

  .bands{position:absolute;left:0;bottom:0;width:100%}
  .bands .band{height:9px}
  .bands .band--green{background:var(--green)}
  .bands .band--yellow{background:var(--yellow);height:10px}

  .divider{position:absolute;left:360px;top:94px;width:1.5px;height:346px;background:var(--rule)}
  .stamp{position:absolute;left:608px;top:42px;width:68px;height:91px}
  .postcode{position:absolute;left:391px;top:195px;display:flex;gap:2px}
  .postcode span{width:20px;height:25px;border:1.5px solid var(--box-edge)}
  .address-lines{position:absolute;left:391px;top:247px;width:284px}
  .address-lines span{display:block;height:32px;background:var(--line-fill);margin-bottom:8px}
</style>
</head>
<body>
<div class="canvas">

  <!-- FRONT -->
  <section class="postcard postcard--front">
    <svg class="photo" viewBox="0 0 1162 830" preserveAspectRatio="none">
      <defs>
        <linearGradient id="donation-tones" x1="0" y1="0" x2="0.3" y2="1">
          <stop offset="0" stop-color="#d9cfc6"/>
          <stop offset="0.35" stop-color="#c9a48e"/>
          <stop offset="0.55" stop-color="#7f9bb9"/>
          <stop offset="0.8" stop-color="#a88a6a"/>
          <stop offset="1" stop-color="#c9a47c"/>
        </linearGradient>
        <clipPath id="photo-circle"><circle cx="896" cy="170" r="446"/></clipPath>
      </defs>
      <circle cx="900" cy="160" r="465" fill="var(--pink)"/>
      <circle cx="896" cy="168" r="454" fill="var(--blue)"/>
      <rect x="0" y="0" width="1162" height="830" fill="url(#donation-tones)" clip-path="url(#photo-circle)" role="img" aria-label="Photo: two hands passing folded denim clothing above a cardboard donation box"/>
    </svg>

    <div class="brand" style="top:30px">
      <span class="brand__dot"></span>
      <span class="brand__name">Bright Lantern Youth</span>
    </div>

    <h1 class="headline" style="top:185px">
      <span class="pink">DONATE</span>
      <span class="blue">YOUR CLOTHES</span>
      <span class="pink">TO SAVE LIVES</span>
    </h1>

    <p class="copy" style="top:316px">We provides meals and medical services to<br>children in need in Honduras.</p>

    <div class="services" style="top:354px">
      <svg class="service-icon" viewBox="0 0 56 56" role="img" aria-label="Meals">
        <circle cx="28" cy="28" r="28" fill="var(--green)"/>
        <path d="M12 32h32M14 35q14 8 28 0M18 30q10-8 20 0" fill="none" stroke="#fff" stroke-width="2" stroke-linecap="round"/>
        <path d="M22 22q-2-3 0-6M28 22q-2-3 0-6M34 22q-2-3 0-6" fill="none" stroke="#fff" stroke-width="1.6" stroke-linecap="round"/>
      </svg>
      <svg class="service-icon" viewBox="0 0 56 56" role="img" aria-label="Medical services">
        <circle cx="28" cy="28" r="28" fill="var(--green)"/>
        <path d="M16 15v8q0 8 7 8q7 0 7-8v-8M23 31v6q0 6 6 6q7 0 7-7v-8" fill="none" stroke="#fff" stroke-width="2.2" stroke-linecap="round"/>
        <circle cx="36" cy="24" r="3.5" fill="none" stroke="#fff" stroke-width="2"/>
        <path d="M29 33v8M25 37h8" stroke="#e63a3a" stroke-width="2.6"/>
      </svg>
    </div>

    <p class="copy" style="top:416px">Collecting unwanted second-hand clothing<br>generates revenue that helps fund the mission<br>and programs run by our foundation.</p>

    <div class="bands"><div class="band band--green"></div><div class="band band--yellow"></div></div>
  </section>

  <!-- BACK -->
  <section class="postcard postcard--back">
    <div class="brand" style="top:22px">
      <span class="brand__dot"></span>
      <span class="brand__name">Bright Lantern Youth</span>
    </div>

    <h2 class="headline" style="top:140px">
      <span class="pink">DONATE</span>
      <span class="blue">YOUR CLOTHES</span>
      <span class="pink">TO SAVE LIFES</span>
    </h2>

    <p class="copy" style="top:264px">We provides meals and medical services to<br>children in need in Honduras.</p>

    <div class="services" style="top:300px;left:32px;gap:14px">
      <svg class="service-icon" viewBox="0 0 56 56" role="img" aria-label="Meals">
        <circle cx="28" cy="28" r="28" fill="var(--green)"/>
        <path d="M12 32h32M14 35q14 8 28 0M18 30q10-8 20 0" fill="none" stroke="#fff" stroke-width="2" stroke-linecap="round"/>
        <path d="M22 22q-2-3 0-6M28 22q-2-3 0-6M34 22q-2-3 0-6" fill="none" stroke="#fff" stroke-width="1.6" stroke-linecap="round"/>
      </svg>
      <svg class="service-icon" viewBox="0 0 56 56" role="img" aria-label="Medical services">
        <circle cx="28" cy="28" r="28" fill="var(--green)"/>
        <path d="M16 15v8q0 8 7 8q7 0 7-8v-8M23 31v6q0 6 6 6q7 0 7-7v-8" fill="none" stroke="#fff" stroke-width="2.2" stroke-linecap="round"/>
        <circle cx="36" cy="24" r="3.5" fill="none" stroke="#fff" stroke-width="2"/>
        <path d="M29 33v8M25 37h8" stroke="#e63a3a" stroke-width="2.6"/>
      </svg>
    </div>

    <p class="copy" style="top:360px">Collecting unwanted second-hand clothing<br>generates revenue that helps fund the mission<br>and programs run by our foundation.</p>

    <div class="divider"></div>

    <svg class="stamp" viewBox="0 0 68 91">
      <rect x="2" y="2" width="64" height="87" fill="#fff" stroke="#888" stroke-width="1.2" stroke-dasharray="3 2.5"/>
      <path d="M26 87L62 52V87Z" fill="#efefef"/>
    </svg>

    <div class="postcode">
      <span></span><span></span><span></span><span></span><span></span>
      <span></span><span></span><span></span><span></span><span></span>
    </div>

    <div class="address-lines"><span></span><span></span><span></span><span></span><span></span></div>
  </section>

</div>
</body>
</html>
```